Business Card Design

we are a brand new cable TV network devoted to self improvement and leading a better life called FLOURIVO TV.I have a logo. We have 3 executives that need cards.I want it to be a heavy stock card: professional but showing our creative nature

Industry/Entity Type

Business

Contact Information for Business Card

CLAUDIA SAENZ AMLIECEO350 San Juan DrPonte Vedra Beach FL 32082904-473-5953

```html
<!DOCTYPE html>
<html lang="en">
<head>
<meta charset="utf-8">
<title>Flourivo TV – Business Card</title>
<link rel="stylesheet" href="https://fonts.googleapis.com/css2?family=Source+Sans+3:wght@400;600;700&display=swap">
<style>
  :root {
    --backdrop: #e9e9e9;
    --card: #ffffff;
    --ink: #231f20;
    --brand-red: #b81f2a;
    --brand-red-bright: #e0222c;
    --brand-red-dark: #8f1820;
    --rule: #8a8a8a;
  }
  * { margin: 0; padding: 0; box-sizing: border-box; }
  html, body {
    width: 1105px;
    height: 1200px;
    overflow: hidden;
    background: var(--backdrop);
  }
  .canvas {
    position: relative;
    width: 1105px;
    height: 1200px;
  }
  .business-card {
    position: absolute;
    left: 72px;
    top: 326px;
    width: 960px;
    height: 548px;
    background: var(--card);
    font-family: "Source Sans 3", "Myriad Pro", Arial, sans-serif;
    color: var(--ink);
  }
  .brand-name {
    position: absolute;
    left: 0;
    right: 0;
    top: 112px;
    display: flex;
    justify-content: center;
    align-items: center;
    gap: 22px;
  }
  .brand-mark {
    width: 60px;
    height: 60px;
    background: var(--brand-red);
  }
  .brand-wordmark {
    font-size: 104px;
    font-weight: 600;
    line-height: 1;
    letter-spacing: -1px;
    color: var(--ink);
  }
  .holder {
    position: absolute;
    right: calc(960px - 438px);
    top: 332px;
    text-align: right;
  }
  .holder-name {
    font-size: 29px;
    font-weight: 700;
    color: var(--brand-red);
    letter-spacing: 0.3px;
    white-space: nowrap;
  }
  .holder-title {
    margin-top: 6px;
    font-size: 26px;
    font-weight: 400;
  }
  .divider {
    position: absolute;
    left: 470px;
    top: 315px;
    width: 1px;
    height: 108px;
    background: var(--rule);
  }
  .contact {
    position: absolute;
    left: 502px;
    top: 314px;
    font-size: 26px;
    line-height: 35px;
    font-style: normal;
  }
  .contact-phone {
    display: flex;
    align-items: center;
    gap: 10px;
    margin-left: 1px;
  }
  .phone-icon { width: 20px; height: 20px; }
  .card-band {
    position: absolute;
    left: 0;
    bottom: 0;
    width: 960px;
    height: 37px;
    display: block;
  }
</style>
</head>
<body>
<main class="canvas">
  <section class="business-card" aria-label="Flourivo TV business card">
    <header class="brand-name">
      <span class="brand-mark" aria-hidden="true"></span>
      <span class="brand-wordmark">FLOURIVO TV</span>
    </header>

    <div class="holder">
      <p class="holder-name">MIRELLA OKAFOR DUNST</p>
      <p class="holder-title">CEO</p>
    </div>

    <span class="divider" aria-hidden="true"></span>

    <address class="contact">
      <p>718 Harlow Creek Dr</p>
      <p>Ponte Vedra Beach FL 32097</p>
      <p class="contact-phone">
        <svg class="phone-icon" viewBox="0 0 24 24" aria-hidden="true">
          <path fill="#b81f2a" d="M6.6 10.8a15.1 15.1 0 0 0 6.6 6.6l2.2-2.2a1 1 0 0 1 1-.25 11.4 11.4 0 0 0 3.6.57 1 1 0 0 1 1 1V20a1 1 0 0 1-1 1A17 17 0 0 1 3 4a1 1 0 0 1 1-1h3.5a1 1 0 0 1 1 1c0 1.25.2 2.45.57 3.57a1 1 0 0 1-.25 1z"/>
        </svg>
        <span>904-618-2047</span>
      </p>
    </address>

    <svg class="card-band" viewBox="0 0 960 37" preserveAspectRatio="none" aria-hidden="true">
      <defs>
        <linearGradient id="band-red" x1="0" x2="1" y1="0" y2="0">
          <stop offset="0" stop-color="#8f1820"/>
          <stop offset="0.55" stop-color="#e0222c"/>
          <stop offset="1" stop-color="#9a1a22"/>
        </linearGradient>
      </defs>
      <polygon points="0,0 628,0 618,37 0,37" fill="url(#band-red)"/>
      <polygon points="636,0 960,0 960,37 626,37" fill="#231f20"/>
    </svg>
  </section>
</main>
</body>
</html>
```